Book cover needed for self help business book

Book cover needed and I will provide back cover blurb and barcode to the winning designer. Book may be too small for spine, but I will give you the page number details to confirm. Book information below:

Title: Nine Winters a Trader
Subtitle: Proven Market Methods That Keep Paying Off Now
Author: Maribel Okonte

Design should be clean, modern, and bold—something that appeals to everyday entrepreneurs and resellers. The cover should reflect grit, real-world hustle, and long-term wisdom without looking overly corporate or flashy. I am open to your creative ideas.

I am open to modern designs, but also designs of rugged old covers that simulate a book that may have aged over the years.

I prefer not to have pictures or silhouettes of people

Requirements
Nice to have
• I am open to modern designs, but also designs of rugged old covers that simulate a book that may have aged over the years.
Should not have
• Pictures or silhouettes of people

```html
<!DOCTYPE html>
<html lang="en">
<head>
<meta charset="utf-8">
<title>Nine Winters a Trader — Maribel Okonte</title>
<link rel="stylesheet" href="https://fonts.googleapis.com/css2?family=Anton&family=Oswald:wght@500&family=Montserrat:wght@800&display=swap">
<style>
  :root {
    --paper: #e9e8e5;
    --ink: #333333;
    --ink-deep: #2b2b2b;
    --white: #f4f3f0;
    --red: #8e2626;
    --tan: #d9c9a6;
    --pink: #e07b7b;
  }
  * { margin: 0; padding: 0; box-sizing: border-box; }
  html, body { width: 840px; height: 1200px; overflow: hidden; background: var(--paper); }
  .cover {
    position: relative;
    width: 840px;
    height: 1200px;
    overflow: hidden;
    background: linear-gradient(to bottom, var(--paper) 0 596px, var(--ink) 596px 100%);
  }

  /* Title stack: sits on the split line, mirrored below it */
  .title-stack {
    position: absolute;
    left: 50%;
    top: 596px;
    width: 380px;
    transform: translate(-50%, -100%);
    display: flex;
    flex-direction: column;
    align-items: center;
    font-family: "Anton", "Impact", sans-serif;
    text-transform: uppercase;
    color: var(--ink-deep);
    line-height: 0.88;
    text-align: center;
  }
  .title-stack .line-big { font-size: 212px; letter-spacing: -2px; }
  .title-stack .line-mid { font-size: 86px; letter-spacing: -1px; margin-top: 6px; }
  .title-stack .line-end { font-size: 124px; letter-spacing: -1px; margin-top: 4px; }
  .title-stack--mirror {
    color: var(--white);
    transform-origin: 50% 100%;
    transform: translate(-50%, -100%) rotate(180deg);
  }

  /* Credits: subtitle + author, mirrored at the top */
  .credits {
    position: absolute;
    left: 0;
    width: 840px;
    top: 1000px;
    text-align: center;
  }
  .credits .subtitle {
    font-family: "Oswald", "Arial Narrow", sans-serif;
    font-weight: 500;
    font-size: 23px;
    letter-spacing: 0.3px;
    text-transform: uppercase;
    color: var(--white);
  }
  .credits .subtitle .accent { color: var(--tan); }
  .credits .author {
    margin-top: 4px;
    font-family: "Montserrat", "Arial", sans-serif;
    font-weight: 800;
    font-size: 38px;
    letter-spacing: 1px;
    text-transform: uppercase;
    color: var(--pink);
  }
  .credits--mirror {
    transform-origin: 50% 0;
    top: 1000px;
    transform: translateY(-808px) rotate(180deg);
  }
  .credits--mirror .subtitle, .credits--mirror .subtitle .accent { color: var(--red); }
  .credits--mirror .author { color: var(--ink-deep); }
</style>
</head>
<body>
  <main class="cover">
    <div class="credits credits--mirror" aria-hidden="true">
      <p class="subtitle">Proven Market Methods That Keep Paying <span class="accent">Off Now</span></p>
      <p class="author">Maribel Okonte</p>
    </div>

    <h1 class="title-stack">
      <span class="line-big">Nine</span>
      <span class="line-mid">Winters a</span>
      <span class="line-end">Trader</span>
    </h1>

    <div class="title-stack title-stack--mirror" aria-hidden="true">
      <span class="line-big">Nine</span>
      <span class="line-mid">Winters a</span>
      <span class="line-end">Trader</span>
    </div>

    <div class="credits">
      <p class="subtitle">Proven Market Methods That Keep Paying <span class="accent">Off Now</span></p>
      <p class="author">Maribel Okonte</p>
    </div>
  </main>
</body>
</html>
```